Label and logo design for an all natural organic skincare product

We need a label design for a new company in the natural beauty space. The company is called "Vessa Kell". "Vessa" refers to the olive tree. "Kell" symbolizes the wren bird. The company name represents purity, nature, and freedom.

Our first product is tamanu oil - a 100% pure, organic, unrefined, cold pressed oil that is be used to improve various skin conditions (acne, eczema, scars, anti-aging) hair, and nails. Tamanu oil is a wonderful skin care healing agent that fades scars, rejuvenates skin cells, and is a powerful natural anti-aging product.

We currently do not have a company logo. We would like the logo and label to be designed together for a coordinated, well thought out, look.

We are looking for a label and logo that convey a high end quality product. We use premium quality all natural ingredients only.

Label size is 10.2cm (wide) x 4.5cm (height). The label wraps around a small amber colored glass bottle with a dropper similar to the images attached. The bottle holds 1oz (30ml) of oil.

Label will contain:
- Company logo
- Product name - "100% Pure Organic Tamanu Oil"
- Quantity - "1 fl oz / 30 ml"
- Ingredients - "100% pure virgin organic cold pressed tamanu oil (calophyllum inophyllum)
- Product Usage - "Dab a few drops of Vessa Kell tamanu oil into your hands and rub the oil into your skin or hair 1 - 3 times a day."
- UPC barcode - will provide later
- Company info:
"Vessa Kell
Atlanta, GA
www.vessakell.example"
- Warning - "For external use only. Do not use if you have allergies to nuts of any kind. Keep out of reach of children."

We've attached a couple images of labels that we like. In general, we prefer a modern, minimalistic, pure look but we are open to your ideas and creativity.

Colors we like: blue-green (think torquoise or tiffany blue), green, grey, white.

If you have any questions, about the design please let me know. The winning designer will be required to do a few additional tweaks to finalize the product. Thank you for your time and happy designing!

```html
<!DOCTYPE html>
<html lang="en">
<head>
<meta charset="utf-8">
<title>Vessa Kell – Tamanu Oil Label and Logo</title>
<link rel="stylesheet" href="https://fonts.googleapis.com/css2?family=Fraunces:opsz,wght@9..144,700&family=Lato:wght@400;700&family=Tinos:ital@0;1&display=swap">
<style>
  :root {
    --lime: #b3c91c;
    --frame-grey: #6b6b6b;
    --ink: #141414;
    --paper: #ffffff;
    --body-text: #1e1e1e;
  }
  * { box-sizing: border-box; margin: 0; padding: 0; }
  html, body { width: 1200px; height: 2217px; overflow: hidden; background: var(--paper); }
  .canvas { position: relative; width: 1200px; height: 2217px; }

  .brand-name {
    font-family: "Fraunces", Georgia, serif;
    font-weight: 700;
    color: var(--paper);
    text-align: center;
    line-height: 0.9;
  }

  .logo-box {
    position: absolute;
    border: solid var(--frame-grey);
    background: var(--lime);
    display: flex;
    flex-direction: column;
    justify-content: center;
    align-items: center;
  }

  /* Bottle label, flat */
  .bottle-label {
    position: absolute;
    left: 80px; top: 640px;
    width: 400px; height: 640px;
    background: var(--paper);
    border: 1px solid #e2e2e2;
  }
  .bottle-label .logo-box {
    left: 110px; top: 70px; width: 180px; height: 170px; border-width: 8px;
  }
  .bottle-label .brand-name { font-size: 56px; }
  .label-band {
    position: absolute; left: 0; right: 0;
    background: var(--lime);
    text-align: center;
    color: var(--paper);
  }
  .bottle-label .label-band { top: 300px; height: 270px; padding-top: 24px; }
  .product-kicker { font-family: "Lato", Arial, sans-serif; font-size: 28px; }
  .product-name {
    font-family: "Fraunces", Georgia, serif; font-weight: 700;
    line-height: 1.05; margin-top: 16px;
  }
  .bottle-label .product-name { font-size: 62px; }
  .quantity-strip {
    position: absolute; left: 0; right: 0;
    background: var(--ink); color: var(--paper);
    font-family: "Lato", Arial, sans-serif; font-weight: 700;
    text-align: center;
  }
  .bottle-label .quantity-strip { top: 570px; height: 50px; line-height: 50px; font-size: 22px; }

  /* Box front panel, flat */
  .box-front {
    position: absolute;
    left: 560px; top: 60px;
    width: 530px; height: 1280px;
    background: var(--paper);
    border: 1px solid #e2e2e2;
  }
  .box-front .logo-box {
    left: 95px; top: 90px; width: 340px; height: 300px; border-width: 14px;
  }
  .box-front .brand-name { font-size: 108px; }
  .box-front .label-band { top: 460px; height: 300px; padding-top: 36px; }
  .box-front .product-kicker { font-size: 32px; }
  .box-front .product-name { font-size: 86px; margin-top: 18px; }
  .product-blurb {
    position: absolute; left: 40px; right: 40px; top: 820px;
    font-family: "Tinos", "Times New Roman", serif;
    font-size: 29px; line-height: 1.22;
    color: var(--body-text); text-align: center;
  }
  .drop-cap { font-style: italic; font-size: 56px; line-height: 0.8; }
  .box-front .quantity-strip { top: 1170px; height: 72px; line-height: 72px; font-size: 26px; }

  /* Standalone logo */
  .logo-sheet {
    position: absolute;
    left: 146px; top: 1436px;
    width: 944px; height: 732px;
    border-width: 34px;
  }
  .logo-sheet .brand-name { font-size: 250px; line-height: 0.95; }
</style>
</head>
<body>
<main class="canvas">

  <section class="bottle-label" aria-label="Bottle label">
    <div class="logo-box">
      <div class="brand-name">Vessa<br>Kell</div>
    </div>
    <div class="label-band">
      <p class="product-kicker">100% Pure Organic</p>
      <h1 class="product-name">Tamanu<br>Oil</h1>
    </div>
    <div class="quantity-strip">1 fl oz / 30 ml</div>
  </section>

  <section class="box-front" aria-label="Carton front panel">
    <div class="logo-box">
      <div class="brand-name">Vessa<br>Kell</div>
    </div>
    <div class="label-band">
      <p class="product-kicker">100% Pure Organic</p>
      <h2 class="product-name">Tamanu<br>Oil</h2>
    </div>
    <p class="product-blurb"><span class="drop-cap">T</span>amanu oil is<br>a wonderful skin care healing<br>agent that fades scars, rejuvenates<br>skin cells and is a powerful natural<br>anti-aging product.<br>Helps improve various skin<br>conditions (acne, eczema, scars,<br>anti-aging) hair and nails.</p>
    <div class="quantity-strip">1 fl oz / 30 ml</div>
  </section>

  <section class="logo-box logo-sheet" aria-label="Vessa Kell logo">
    <div class="brand-name">Vessa<br>Kell</div>
  </section>

</main>
</body>
</html>
```